Now Leasing Banner

Looking for a banner that says the following information approx 4' x 30'

Now Leasing Maplewood Terrace 925-318-6054

Target Market(s)

Drive by traffic

Industry/Entity Type

Residential property management

Requirements
Must have
• Clear and readable from a distance

```html
<!DOCTYPE html>
<html lang="en">
<head>
<meta charset="UTF-8">
<title>Now Leasing – Maplewood Terrace</title>
<link rel="stylesheet" href="https://fonts.googleapis.com/css2?family=Anton&family=Oswald:wght@500;700&display=swap">
<style>
  :root {
    --brand-red: #a50000;
    --headline-yellow: #f2fc12;
    --paper-white: #ffffff;
    --ink-black: #111111;
    --drop-shadow: rgba(40, 40, 50, 0.55);
  }
  html, body {
    margin: 0;
    padding: 0;
    width: 1200px;
    height: 213px;
    overflow: hidden;
    background: var(--paper-white);
  }
  .banner {
    position: absolute;
    left: 40px;
    top: 21px;
    width: 1065px;
    height: 138px;
    display: flex;
    box-shadow: 10px 11px 9px var(--drop-shadow);
  }
  .banner__title-panel {
    width: 503px;
    background: var(--brand-red);
    display: flex;
    flex-direction: column;
    align-items: center;
    justify-content: flex-start;
  }
  .banner__headline {
    margin: 6px 0 0;
    font-family: "Oswald", sans-serif;
    font-weight: 700;
    font-size: 66px;
    line-height: 72px;
    letter-spacing: 0.09em;
    padding-left: 0.09em;
    color: var(--headline-yellow);
  }
  .banner__property {
    margin: -6px 0 0;
    font-family: "Oswald", sans-serif;
    font-weight: 500;
    font-size: 44px;
    line-height: 52px;
    color: var(--paper-white);
  }
  .banner__phone-panel {
    flex: 1;
    background: var(--paper-white);
    display: flex;
    align-items: center;
    justify-content: center;
  }
  .banner__phone {
    margin: 0;
    font-family: "Anton", sans-serif;
    font-size: 100px;
    line-height: 1;
    color: var(--brand-red);
    text-shadow: 3px 3px 0 var(--ink-black);
    transform: scaleX(0.86);
    letter-spacing: -0.01em;
  }
</style>
</head>
<body>
  <div class="banner">
    <div class="banner__title-panel">
      <p class="banner__headline">NOW LEASING</p>
      <p class="banner__property">Maplewood Terrace</p>
    </div>
    <div class="banner__phone-panel">
      <p class="banner__phone">925-318-6054</p>
    </div>
  </div>
</body>
</html>
```